Word Page Templates x 5

1 x Letterhead Template with Header and Footer able to be printed to paper and pdf with non blurry resolution
- File attached looks ok on computer screen but does not print the same
- We are wanting it to print like it looks on the screen
- We are wanting it to print not fuzzy in resolution
- We are wanting the banner to be on the absolute edge of the page like it is on the computer screen
- We are needing to print this to paper and pdf with perfect resolution and colour

Please can someone help us!!

I have provided the logo files in our posession. If better resolutions are required please let us know.

We are also wanting 4 simple page templates to be setup in Landscape and Portrait orientation as well once we are happy with the letterhead that is provided samples have been provided
Updates

Hi all I have the vector files available now along with a Colour profile

Requirements
Must have
• Clear when printed on A4 Paper
Should not have
• Blurry images, Colour must be correct (same as Logo) - Please reference our website if need be ..... lomvira.com.au

```html
<!DOCTYPE html>
<html lang="en">
<head>
<meta charset="utf-8">
<title>Lomvira Letterhead Set</title>
<link rel="stylesheet" href="https://fonts.googleapis.com/css2?family=Nunito+Sans:wght@400;800&display=swap">
<style>
  :root {
    --backdrop: #d2d3d5;
    --paper: #ffffff;
    --brand-blue: #15568f;
    --brand-orange: #e8893b;
    --brand-navy: #2b2a7c;
    --text-light: #ffffff;
  }
  html, body {
    margin: 0;
    padding: 0;
    width: 1200px;
    height: 793px;
    overflow: hidden;
    background: var(--backdrop);
    font-family: "Nunito Sans", Arial, sans-serif;
  }
  .canvas {
    position: relative;
    width: 1200px;
    height: 793px;
  }
  .sheet {
    position: absolute;
    display: block;
    background: var(--paper);
  }
  .sheet--portrait { left: 152px; top: 146px; width: 354px; height: 501px; }
  .sheet--landscape { left: 547px; top: 219px; width: 501px; height: 354px; }
  .band { fill: var(--brand-blue); }
  .accent-line { fill: none; stroke: var(--brand-orange); stroke-width: 1.4; }
  .contact-label { fill: var(--text-light); font-size: 10px; font-weight: 800; }
  .contact-value { fill: var(--text-light); font-size: 10px; font-weight: 400; }
  .member-mark { fill: var(--brand-orange); }
  .member-title { fill: var(--brand-navy); font-size: 19px; font-weight: 800; }
  .member-name { fill: var(--brand-navy); font-size: 8.4px; font-weight: 800; }
</style>
</head>
<body>
<main class="canvas">

  <!-- Portrait letterhead -->
  <svg class="sheet sheet--portrait" viewBox="0 0 701 991" aria-label="Portrait letterhead">
    <rect width="701" height="991" fill="var(--paper)"/>
    <g class="member-badge">
      <circle class="member-mark" cx="127" cy="72" r="34"/>
      <text class="member-title" x="127" y="142" text-anchor="middle">MEMBER</text>
      <text class="member-name" x="127" y="153" text-anchor="middle">LOMVIRA LINE MARKING</text>
      <text class="member-name" x="127" y="163" text-anchor="middle">ASSOCIATION</text>
    </g>
    <path class="band header-band" d="M701 46 H322 Q310 46 305 57 L264 151 Q260 163 272 163 H701 Z"/>
    <path class="accent-line header-line" d="M701 33 H258 Q245 33 251 44 L295 116 Q314 149 347 149 H701"/>
    <g class="contact-block">
      <text class="contact-label" x="402" y="79">A.</text><text class="contact-value" x="424" y="79">18B Harlow Street, Bayside, Vic 3190</text>
      <text class="contact-label" x="402" y="97">P.</text><text class="contact-value" x="424" y="97">1300 482 716</text>
      <text class="contact-label" x="402" y="115">E.</text><text class="contact-value" x="424" y="115">info@lomvira.com.au</text>
      <text class="contact-label" x="402" y="132">W.</text><text class="contact-value" x="424" y="132">www.lomvira.com.au</text>
    </g>
    <path class="band footer-band" d="M0 966 H666 Q684 966 701 991 H0 Z"/>
    <path class="accent-line footer-line" d="M0 956 H638 Q652 956 645 968 L634 991"/>
  </svg>

  <!-- Landscape letterhead -->
  <svg class="sheet sheet--landscape" viewBox="0 0 991 701" aria-label="Landscape letterhead">
    <rect width="991" height="701" fill="var(--paper)"/>
    <g class="member-badge">
      <circle class="member-mark" cx="147" cy="64" r="34"/>
      <text class="member-title" x="145" y="134" text-anchor="middle">MEMBER</text>
      <text class="member-name" x="145" y="145" text-anchor="middle">LOMVIRA LINE MARKING</text>
      <text class="member-name" x="145" y="155" text-anchor="middle">ASSOCIATION</text>
    </g>
    <path class="band header-band" d="M991 39 H436 Q424 39 419 50 L378 144 Q374 155 386 155 H991 Z"/>
    <path class="accent-line header-line" d="M991 26 H370 Q357 26 364 37 L407 109 Q427 142 460 142 H991"/>
    <g class="contact-block">
      <text class="contact-label" x="488" y="88">A.</text><text class="contact-value" x="509" y="88">18B Harlow Street, Bayside, Vic 3190</text>
      <text class="contact-label" x="488" y="106">P.</text><text class="contact-value" x="509" y="106">1300 482 716</text>
      <text class="contact-label" x="764" y="88">E.</text><text class="contact-value" x="786" y="88">info@lomvira.com.au</text>
      <text class="contact-label" x="764" y="106">W.</text><text class="contact-value" x="786" y="106">www.lomvira.com.au</text>
    </g>
    <path class="band footer-band" d="M0 676 H910 Q934 676 956 701 H0 Z"/>
    <path class="accent-line footer-line" d="M0 667 H896 Q910 667 903 679 L893 701"/>
  </svg>

</main>
</body>
</html>
```